Birthday Card Design

I need a birthday card designed for my son's 7th birthday party. It needs to be a colorful, inviting, maybe fun but definitely a memorable birthday card. I would like it to be different from the normal birthday card templates I see on the Internet.
Updates

As requested, I have uploaded 3 pictures of Tovik for use as a sketch etc. Preferably, pls do not use any picture as is in the card.

Target Market(s)

My son's friends are either his classmates or children of our friends. The kid would be fairly mixed nationalities - (Indian, English, American, Chinese, Japanese and Dutch and maybe some more)The party will be in a hall (about 50x40 feet) and there will be a magician, juggler, balloon sculpting, face painting kind of entertainment. Overall we expect to have about 30-40 children at the party and including adults about 100 people total.

Industry/Entity Type

Internet

Requirements
Must have
• I am planning to have a 4 side A5 layout but am open to 2 side A5 or A4 size also. It must be folded A5 or A4 definitely because of Singapore post office limitations for bulk mailing. My Son's name is Tovik. He is turning 7 in January. The party is on 15th January from 7.00 PM to 9.00 PM.

```html
<!DOCTYPE html>
<html lang="en">
<head>
<meta charset="utf-8">
<title>Tovik's 7th Birthday Party Invitation</title>
<link rel="stylesheet" href="https://fonts.googleapis.com/css2?family=Caprasimo&family=Fredoka:wght@700&display=swap">
<style>
  :root {
    --burst-blue: #1f4fe0;
    --burst-violet: #7a2bd8;
    --burst-magenta: #d81f9a;
    --burst-pink: #f060b8;
    --burst-red: #c8102e;
    --ink-plum: #6b0f5e;
    --ink-royal: #1730e0;
    --ink-grape: #5a1aa8;
    --ink-berry: #8a1490;
    --ink-crimson: #b3102a;
    --ink-sky: #1c86f2;
    --ink-black: #111111;
    --glow: #ffffff;
    --frame-dark: #7a0c3c;
    --frame-mid: #c0206a;
  }
  * { margin: 0; padding: 0; box-sizing: border-box; }
  html, body { width: 1200px; height: 852px; overflow: hidden; background: #ffffff; }
  .invitation {
    position: relative;
    width: 1200px;
    height: 852px;
    overflow: hidden;
    background:
      radial-gradient(ellipse at 62% 35%, rgba(255,255,255,0.75) 0%, rgba(255,200,240,0.45) 18%, rgba(255,255,255,0) 45%),
      linear-gradient(115deg, var(--burst-blue) 0%, var(--burst-violet) 25%, var(--burst-magenta) 50%, var(--burst-pink) 68%, var(--burst-red) 100%);
    font-family: "Caprasimo", "Cooper Black", serif;
  }
  .headline {
    position: absolute;
    left: 0;
    width: 570px;
    text-align: center;
    line-height: 1;
    text-shadow:
      0 0 3px var(--glow), 0 0 6px var(--glow), 0 0 10px var(--glow),
      2px 2px 0 var(--glow), -2px -2px 0 var(--glow), 2px -2px 0 var(--glow), -2px 2px 0 var(--glow);
  }
  .headline--tagline-top { top: 100px; font-size: 62px; color: var(--ink-plum); letter-spacing: 1px; }
  .headline--tagline-bottom { top: 160px; font-size: 76px; color: var(--ink-royal); }
  .headline--age {
    top: 240px; font-size: 270px; letter-spacing: -6px;
    background: linear-gradient(90deg, var(--ink-grape) 0%, var(--ink-berry) 100%);
    -webkit-background-clip: text; background-clip: text; color: transparent;
    text-shadow: none;
    filter: drop-shadow(0 0 3px var(--glow)) drop-shadow(0 0 6px var(--glow));
  }
  .headline--date { top: 505px; font-size: 82px; color: var(--ink-crimson); }
  .headline--time {
    top: 612px; font-family: "Fredoka", "Arial Rounded MT Bold", sans-serif;
    font-size: 48px; color: var(--ink-sky);
  }
  .invited {
    position: absolute;
    left: 615px; top: 40px; width: 560px;
    text-align: center;
    font-size: 44px; color: var(--ink-royal); letter-spacing: 2px;
    transform: rotate(-6deg);
    text-shadow: 0 0 4px var(--glow), 0 0 8px var(--glow), 2px 2px 0 var(--glow), -2px -2px 0 var(--glow);
  }
  .portrait-frame {
    position: absolute;
    left: 630px; top: 110px; width: 540px; height: 540px;
  }
  .party-name {
    position: absolute;
    left: 615px; width: 570px; text-align: center; line-height: 1;
    text-shadow:
      0 0 3px var(--glow), 0 0 7px var(--glow),
      2px 2px 0 var(--glow), -2px -2px 0 var(--glow), 2px -2px 0 var(--glow), -2px 2px 0 var(--glow);
  }
  .party-name--owner { top: 640px; font-size: 76px; color: var(--ink-crimson); }
  .party-name--event { top: 738px; font-size: 62px; color: var(--ink-black); }
</style>
</head>
<body>
  <main class="invitation">
    <h2 class="headline headline--tagline-top">OUT OF THIS</h2>
    <h2 class="headline headline--tagline-bottom">WORLD FUN!</h2>
    <h1 class="headline headline--age">7th</h1>
    <p class="headline headline--date">January 15th</p>
    <p class="headline headline--time">7.00 PM to 9.00 PM</p>

    <p class="invited">YOU ARE INVITED!</p>

    <svg class="portrait-frame" viewBox="0 0 540 540" width="540" height="540">
      <defs>
        <radialGradient id="frameRing" cx="50%" cy="45%" r="55%">
          <stop offset="70%" stop-color="var(--frame-mid)"/>
          <stop offset="100%" stop-color="var(--frame-dark)"/>
        </radialGradient>
        <linearGradient id="portraitFill" x1="0" y1="0" x2="0" y2="1">
          <stop offset="0%" stop-color="#4a3a5a"/>
          <stop offset="45%" stop-color="#b08878"/>
          <stop offset="100%" stop-color="#e8e0b0"/>
        </linearGradient>
      </defs>
      <ellipse cx="270" cy="262" rx="232" ry="262" fill="url(#frameRing)" opacity="0.85"/>
      <ellipse cx="270" cy="262" rx="204" ry="238" fill="none" stroke="#ffffff" stroke-opacity="0.35" stroke-width="4"/>
      <ellipse cx="270" cy="262" rx="178" ry="242" fill="url(#portraitFill)"
               role="img" aria-label="Portrait photo of the birthday boy, Tovik"/>
      <ellipse cx="270" cy="262" rx="178" ry="242" fill="none" stroke="var(--frame-dark)" stroke-width="5"/>
    </svg>

    <p class="party-name party-name--owner">Tovik’s 7th</p>
    <p class="party-name party-name--event">Birthday Party!</p>
  </main>
</body>
</html>
```